Business card for a Exhibition booth fabrication company

Hi. My company would like to change our corporate name card. We are an events and Exhibition stand builder company. We would like our corporate name card to resonate what we do. I need someone to create something unique that relates to the industry that I am in. The graphic designer should be creative to incorporate the elements of my industry and try to blend in well in the design of the card. Our aim is to ensure that we are unique and our card can look different from our competitors.
Updates

The decision maker was very busy and didnt had time to make this decision

Target Market(s)

Marketing and events manager from all companies

Contact Information for Business Card

The business card should have the following details:
Name
Job Title
Email
Website

Colors

Designer to choose colors to be used in the design.

Requirements
Must have
• The card must be look something that is relevant to the service that I am providing. My website is: www.velmora-buildworks.example
• You can see my website to get more information on what service that I am doing
Nice to have
• On the back of my card, I would like to have a globe image with the incorporation of my company logo. This is to indicate that my services can be done in any part of the world.

```html
<!DOCTYPE html>
<html lang="en">
<head>
<meta charset="utf-8">
<title>Velmora Buildworks – Business Card</title>
<link href="https://fonts.googleapis.com/css2?family=Questrial&display=swap" rel="stylesheet">
<style>
  :root {
    --page-bg: #f1f1f1;
    --card-bg: #ffffff;
    --brand-red: #ec1c24;
    --slate: #646567;
    --text-grey: #555658;
    --map-tint: #ececec;
    --white: #ffffff;
  }
  * { margin: 0; padding: 0; box-sizing: border-box; }
  html, body { width: 1200px; height: 1000px; overflow: hidden; }
  body {
    background: var(--page-bg);
    font-family: "Questrial", "Century Gothic", sans-serif;
    position: relative;
  }
  .card {
    position: absolute;
    left: 332px;
    width: 535px;
    height: 325px;
    background: var(--card-bg);
    box-shadow: 4px 6px 8px rgba(0,0,0,0.22);
    overflow: hidden;
  }
  .card--front { top: 153px; }
  .card--back { top: 525px; height: 323px; }

  .world-map-area {
    position: absolute;
    left: 0; top: 18px;
    width: 310px; height: 230px;
    background: radial-gradient(ellipse at 40% 45%, var(--map-tint) 0%, rgba(236,236,236,0.4) 60%, rgba(255,255,255,0) 80%);
  }
  .feature-panel {
    position: absolute;
    left: 0; top: 0;
    width: 535px; height: 267px;
  }
  .holder-name {
    position: absolute;
    left: 45px; top: 40px;
    font-size: 50px;
    line-height: 1;
    color: var(--brand-red);
  }
  .holder-title {
    position: absolute;
    left: 65px; top: 99px;
    font-size: 29px;
    line-height: 1;
    color: var(--slate);
  }
  .services {
    position: absolute;
    left: 334px; top: 114px;
    list-style: none;
    color: var(--white);
    font-size: 13px;
    line-height: 15.5px;
  }
  .contact-list {
    position: absolute;
    left: 44px; top: 277px;
    list-style: none;
    font-size: 13px;
    color: var(--text-grey);
  }
  .contact-list li {
    display: flex;
    align-items: center;
    height: 21px;
  }
  .contact-list svg { width: 12px; height: 12px; margin-right: 10px; }

  .brand-lockup {
    position: absolute;
    left: 0; right: 0; top: 140px;
    display: flex;
    justify-content: center;
    align-items: center;
    gap: 12px;
  }
  .brand-mark {
    width: 22px; height: 22px;
    background: var(--brand-red);
  }
  .brand-name {
    font-size: 24px;
    letter-spacing: 2px;
    color: var(--slate);
    text-transform: uppercase;
  }
</style>
</head>
<body>
  <section class="card card--front" aria-label="Card front">
    <div class="world-map-area" role="img" aria-label="Faint world map showing global reach"></div>
    <svg class="feature-panel" viewBox="0 0 535 267" aria-hidden="true">
      <rect x="0" y="258" width="535" height="9" fill="var(--brand-red)"/>
      <rect x="250" y="0" width="285" height="267" fill="var(--brand-red)"/>
      <ellipse cx="438" cy="152" rx="140" ry="110" fill="var(--slate)"/>
    </svg>
    <h1 class="holder-name">Name</h1>
    <p class="holder-title">Job Title</p>
    <ul class="services">
      <li>Exhibition Booth Construction</li>
      <li>Creative Signage</li>
      <li>Interior Design</li>
      <li>Exhibition Booth Design</li>
      <li>Installation &amp; Dismmantle</li>
      <li>Outdoor Event Setup</li>
    </ul>
    <ul class="contact-list">
      <li>
        <svg viewBox="0 0 12 12" aria-hidden="true"><rect x="1" y="2.5" width="10" height="7" fill="none" stroke="var(--text-grey)" stroke-width="1"/><path d="M1 2.5 L6 6.5 L11 2.5" fill="none" stroke="var(--text-grey)" stroke-width="1"/></svg>
        info@velmora-buildworks.example
      </li>
      <li>
        <svg viewBox="0 0 12 12" aria-hidden="true"><circle cx="6" cy="6" r="4.5" fill="none" stroke="var(--text-grey)" stroke-width="1"/></svg>
        www.velmora-buildworks.example
      </li>
    </ul>
  </section>

  <section class="card card--back" aria-label="Card back">
    <div class="brand-lockup">
      <span class="brand-mark" aria-hidden="true"></span>
      <span class="brand-name">Velmora Buildworks</span>
    </div>
  </section>
</body>
</html>
```